Business Card Design

We have a group of different function companies owned and operated by one person. We are located in the Dallas Fort Worth area in Texas. We develop properties to where we are owners and develop properties that are not ours as well. We build custom homes and commercial buildings. We also do residential and commercial remodeling. We also own commercial properties in which we lease office space. We are trying to merge all we do into one card and have done so already into one website. We initially had thought of having a logo made with HV in nice attractive lettering maybe as a watermark. We are open to the color scheme but no neons or pastels.

Project Deadline Extended
Reason: I am needing 2 different cards for two businesses.

Industry/Entity Type

Residential

Contact Information for Business Card

Harwell Ventures
4826 Mabry Ln. Suite 417
Keller, Texas 76109
Land Development
Residential and Commercial Construction
Commercial Real Estate
Dale Wintermoot
www.harwellgrp.example
dale@harwellgrp.example
Cell: 817-555-0142
Office: 817-555-0187
Fax: 8175550163

```html
<!DOCTYPE html>
<html lang="en">
<head>
<meta charset="utf-8">
<title>Harwell Ventures – Business Card</title>
<link rel="stylesheet" href="https://fonts.googleapis.com/css2?family=Libre+Baskerville:ital,wght@0,400;0,700;1,400&display=swap">
<style>
  :root {
    --page: #e9e6e1;
    --card-black: #0b0b0b;
    --card-black-sheen: #2a2a2a;
    --card-white: #ffffff;
    --ink: #1a1a1a;
    --ink-soft: #3a3a3a;
    --rule: #111111;
    --silver-light: #e4e4e4;
    --silver-dark: #a9a9a9;
    --sage-light: #eef3dc;
    --sage-mid: #c9d7a3;
    --sage-dark: #9fb27a;
    --white-text: #f4f4f4;
  }
  * { box-sizing: border-box; margin: 0; padding: 0; }
  html, body { width: 1200px; height: 900px; overflow: hidden; }
  body {
    background: var(--page);
    font-family: "Libre Baskerville", "Times New Roman", serif;
    color: var(--ink);
    position: relative;
  }
  .card {
    position: absolute;
    width: 560px;
    height: 320px;
    box-shadow: 0 10px 28px rgba(0,0,0,0.25);
  }

  /* Front */
  .card-front {
    left: 70px; top: 80px;
    background: linear-gradient(115deg, var(--card-black) 0%, var(--card-black) 45%, var(--card-black-sheen) 58%, var(--card-black) 72%);
  }
  .front-mark {
    position: absolute;
    right: 54px; top: 118px;
    display: flex; align-items: center; gap: 14px;
  }
  .front-mark .dot {
    width: 14px; height: 14px; border-radius: 50%;
    background: var(--white-text);
  }
  .front-name {
    color: var(--white-text);
    font-size: 26px;
    letter-spacing: 1px;
    text-transform: uppercase;
  }

  /* Back */
  .card-back {
    left: 570px; top: 500px;
    background: var(--card-white);
    border: 1px solid #d6d6d6;
  }
  .header-band {
    position: absolute;
    left: 18px; top: 16px; width: 524px; height: 132px;
    background: linear-gradient(180deg, var(--silver-light), var(--silver-dark));
  }
  .mark-box {
    position: absolute; left: 0; top: 0; width: 140px; height: 132px;
    display: flex; align-items: center; justify-content: center;
  }
  .mark-box .dot {
    width: 22px; height: 22px; border-radius: 50%;
    background: var(--ink);
  }
  .name-panel {
    position: absolute; left: 140px; top: 0; right: 0; height: 50px;
    background: linear-gradient(180deg, var(--sage-light), var(--sage-mid) 55%, var(--sage-dark));
    display: flex; align-items: center; justify-content: flex-end;
    padding-right: 18px;
    border-bottom: 2px solid #6f6f6f;
  }
  .company-name { font-size: 25px; font-weight: 700; color: var(--ink); }
  .address-panel {
    position: absolute; left: 140px; top: 54px; right: 0; bottom: 22px;
    background: linear-gradient(180deg, var(--sage-mid), var(--sage-light) 50%, var(--sage-mid));
    text-align: right;
    padding: 8px 18px 0 0;
    font-size: 11px; line-height: 1.5; color: var(--ink-soft);
  }
  .address-panel .web { font-weight: 700; color: var(--ink); }
  .services {
    position: absolute; left: 18px; top: 134px; width: 524px;
    display: flex; justify-content: space-between;
    font-size: 9px; font-style: italic; font-weight: 700;
    padding: 0 4px 2px;
    border-bottom: 3px solid var(--rule);
  }
  .contact-lines {
    position: absolute; right: 26px; top: 166px;
    list-style: none; font-size: 12px; line-height: 1.6;
  }
  .contact-lines li { display: flex; align-items: center; gap: 8px; }
  .contact-lines svg { width: 12px; height: 12px; fill: var(--ink-soft); }
  .person { position: absolute; left: 30px; top: 226px; }
  .person-name { font-size: 20px; text-transform: uppercase; letter-spacing: 0.5px; }
  .person-title { font-size: 13px; font-weight: 700; margin-top: 2px; }
  .person-email { display: flex; align-items: center; gap: 7px; font-size: 12px; font-weight: 700; margin-top: 4px; }
  .person-email svg { width: 12px; height: 12px; fill: var(--ink-soft); }
</style>
</head>
<body>
  <section class="card card-front" aria-label="Card front">
    <div class="front-mark">
      <span class="dot"></span>
      <span class="front-name">Harwell Ventures</span>
    </div>
  </section>

  <section class="card card-back" aria-label="Card back">
    <div class="header-band">
      <div class="mark-box"><span class="dot"></span></div>
      <div class="name-panel"><span class="company-name">Harwell Ventures</span></div>
      <div class="address-panel">
        <div>4826 Mabry Ln. Suite 417</div>
        <div>Keller, Texas 76109</div>
        <div class="web">www.harwellgrp.example</div>
      </div>
    </div>
    <div class="services">
      <span>● Land Development</span>
      <span>● Residential and Commercial Construction</span>
      <span>● Commercial Real Estate ●</span>
    </div>
    <ul class="contact-lines">
      <li><svg viewBox="0 0 12 12" aria-label="Cell"><rect x="3" y="0" width="6" height="12" rx="1"/></svg>817-555-0142</li>
      <li><svg viewBox="0 0 12 12" aria-label="Office"><path d="M2 1l3 0 1 3-2 1c1 2 2 3 4 4l1-2 3 1 0 3c-6 0-10-4-10-10z"/></svg>817-555-0187</li>
      <li><svg viewBox="0 0 12 12" aria-label="Fax"><rect x="3" y="0" width="6" height="4"/><rect x="0" y="4" width="12" height="6" rx="1"/></svg>817-555-0163</li>
    </ul>
    <div class="person">
      <div class="person-name">Dale Wintermoot</div>
      <div class="person-title">President</div>
      <div class="person-email"><svg viewBox="0 0 12 12" aria-label="Email"><rect x="0" y="2" width="12" height="8" rx="1"/></svg>dale@harwellgrp.example</div>
    </div>
  </section>
</body>
</html>
```